Divorce marketing brochure - Which will include a toy ball and chain as a gimick

A single page marketing enclosure which includes a toy ball and chain to be given to lawyers. I want to convey the following messages:

1. We pay a 1/3 referral fee;
2. We solve difficult problems.

Examples of problems solved:
*Litigation of complex property, custody, support and parenting time issues;
*Protection (or invasion) of personal injury proceeds in divorce;
*Distribution of consortium proceeds in divorce;
*Pre-nuptial and Post-nuptial agreements.
*Settlements
*Reduce conflict

A sample of the toy ball and chain enclosure can be viewed here:

My website is www.thesplitcounsel.com (currently being updated - who's isn't?)

http://www.shopvexto.com/Orbel-Trinkets-Inc-Convict-Shackle/dp/K7QX3MZP21/ref=sr_1_9?ie=UTF8&qid=1311011554&sr=8-9

Target Market(s)

Personal Injury Attorneys

Industry/Entity Type

Marketing

Requirements
Must have
• Call to action:

www.thesplitcounsel.com
1-877-HIRE-TEAM
248-555-7182
Marcus@brevanlegal.com
Nice to have
• I want this campaign to stand out. Different is good. I am a divorce lawyer marketing to personal injury attorneys (and some others) for divorce referrals. (No one forgets the girl with red hair and braces) I want the campaign to be remembered without being offensive.
Should not have

```html
<!DOCTYPE html>
<html lang="en">
<head>
<meta charset="utf-8">
<title>Referral Fee Brochure</title>
<link href="https://fonts.googleapis.com/css2?family=Oswald:wght@700&family=Roboto+Condensed:wght@300;400;700&display=swap" rel="stylesheet">
<style>
  :root {
    --red: #e3151b;
    --ink: #2a2a2a;
    --white: #ffffff;
    --black: #0d0d0d;
    --sky-top: #ffffff;
    --sky-mid: #7ab8e4;
    --sky-soft: #d6eaf7;
  }
  * { margin: 0; padding: 0; box-sizing: border-box; }
  html, body { width: 847px; height: 1200px; overflow: hidden; background: var(--white); }
  .brochure {
    position: relative;
    width: 847px;
    height: 1200px;
    overflow: hidden;
    background: linear-gradient(180deg, var(--sky-top) 0%, var(--sky-top) 4%, var(--sky-mid) 22%, #a9d2ee 38%, var(--sky-soft) 55%, #f4f9fd 78%, var(--white) 100%);
    font-family: "Roboto Condensed", "Arial Narrow", sans-serif;
  }
  .streaks { position: absolute; left: 0; top: 0; width: 847px; height: 700px; }
  .headline {
    position: absolute; left: 0; top: 22px; width: 847px;
    text-align: center;
    font-family: "Oswald", "Arial Narrow", sans-serif;
    font-weight: 700;
    color: var(--red);
    font-size: 128px;
    line-height: 122px;
    letter-spacing: 1px;
    text-shadow: 0 3px 4px rgba(0,0,0,0.25);
  }
  .rule { position: absolute; left: 0; top: 292px; width: 847px; height: 5px; background: var(--red); }
  .band {
    position: absolute; left: 51px; top: 326px; width: 745px; height: 68px;
    background: var(--red);
    color: var(--white);
    font-family: "Oswald", "Arial Narrow", sans-serif;
    font-weight: 700;
    font-size: 46px;
    line-height: 68px;
    text-align: center;
    letter-spacing: 0.5px;
  }
  .examples-title {
    position: absolute; left: 58px; top: 418px;
    font-weight: 300;
    font-size: 46px;
    line-height: 60px;
    letter-spacing: 4px;
    color: var(--ink);
  }
  .problems {
    position: absolute; top: 496px;
    list-style: none;
    color: var(--ink);
    font-weight: 700;
    font-size: 26px;
    line-height: 31px;
  }
  .problems li { position: relative; padding-left: 18px; margin-bottom: 16px; }
  .problems li::before { content: "\2022"; position: absolute; left: 0; top: 0; }
  .problems--left { left: 58px; width: 400px; }
  .problems--right { left: 466px; width: 370px; }
  .firm-mark {
    position: absolute; left: 51px; top: 752px; width: 284px; height: 124px;
    background: var(--black);
    border: 2px solid #555;
    display: flex; align-items: center; justify-content: center;
    color: var(--white);
    font-weight: 400;
    font-size: 27px;
  }
  .shackle-art {
    position: absolute; left: 0; top: 880px; width: 530px; height: 270px;
    background: radial-gradient(ellipse at 35% 55%, #3a3a3a 0%, #2a2a2a 30%, rgba(60,60,60,0.35) 60%, rgba(255,255,255,0) 78%);
  }
  .cta {
    position: absolute; left: 466px; top: 821px; width: 424px; height: 424px;
    border-radius: 50%;
    background: radial-gradient(circle at 40% 35%, #2b2b2b 0%, var(--black) 70%);
    color: var(--white);
  }
  .cta-inner {
    position: absolute; left: 0; top: 92px; width: 282px; text-align: center;
    font-weight: 700;
    white-space: nowrap;
  }
  .cta-title { font-family: "Oswald", sans-serif; font-size: 32px; line-height: 50px; }
  .cta-url { font-size: 25px; line-height: 40px; }
  .cta-phone { font-family: "Oswald", sans-serif; color: var(--red); font-size: 36px; line-height: 54px; }
  .cta-line { font-size: 30px; line-height: 46px; }
  .cta-email { font-size: 22px; line-height: 40px; font-weight: 400; }
</style>
</head>
<body>
<main class="brochure">
  <svg class="streaks" viewBox="0 0 847 700" aria-hidden="true">
    <path d="M-20 250 Q300 120 880 60" stroke="#ffffff" stroke-opacity="0.35" stroke-width="28" fill="none"/>
    <path d="M-20 420 Q400 300 880 200" stroke="#ffffff" stroke-opacity="0.25" stroke-width="40" fill="none"/>
    <path d="M-20 560 Q420 470 880 380" stroke="#ffffff" stroke-opacity="0.3" stroke-width="18" fill="none"/>
  </svg>

  <h1 class="headline">WE PAY A 1/3<br>REFERRAL FEE</h1>
  <div class="rule"></div>
  <h2 class="band">WE SOLVE DIFFICULT PROBLEMS</h2>

  <h3 class="examples-title">EXAMPLES OF PROBLEMS SOLVED:</h3>
  <ul class="problems problems--left">
    <li>Litigation of complex property,<br>custody, support and parenting<br>time issues</li>
    <li>Protection (or invasion)<br>of personal injury proceeds<br>in divorce</li>
  </ul>
  <ul class="problems problems--right">
    <li>Distribution of consortium<br>proceeds in divorce</li>
    <li>Pre-nuptial and Post-<br>nuptial agreements</li>
    <li>Settlements</li>
    <li>Reduce conflict</li>
  </ul>

  <div class="firm-mark">The Brevan Law Firm</div>

  <div class="shackle-art" role="img" aria-label="Photo of a toy ball and chain with an open shackle cuff"></div>

  <section class="cta">
    <div class="cta-inner">
      <p class="cta-title">CALL TO ACTION:</p>
      <p class="cta-url">www.thesplitcounsel.com</p>
      <p class="cta-phone">1-877-HIRE-TEAM</p>
      <p class="cta-line">248-555-7182</p>
      <p class="cta-email">Marcus@brevanlegal.com</p>
    </div>
  </section>
</main>
</body>
</html>
```